Stationary for Manufacturing Company
Metal Manufacturing
Stationary for Manufacturing Company - Manufacturing
Creative Brief
Professional
Gerald Pinwick
27615 Harlow Ave Unit C Longmont, CO 80519
gpinwick@forgevx.com
www.forgevx.com
Would like stationary designs following our logo design.
gpinwick gpinwick
quillmotions I like #79 & #87 with the solid color. Can you do a these on other stationary objects.
Nook, I really like the stationary on #88 & #89, can you continue the design onto the inside of the folder on the pockets. Also I would like to see Forge Vexa in shading in smaller text like #16 and the large shaded logo removed. Thank you for your submissions.
#129 & #126 I like both of these cards, #129 seems to have to many lines and seems to busy. Can you reduce some of them and do this on other stationary objects as well. Thank you.
#16 I really like how the text Forge Vexa is on the back of the card.Can you put that one in other stationary objects as well. Thank you.

```html
<!DOCTYPE html>
<html lang="en">
<head>
<meta charset="utf-8">
<title>Forge Vexa Business Card</title>
<link href="https://fonts.googleapis.com/css2?family=Roboto:wght@400;500;700&display=swap" rel="stylesheet">
<style>
  :root {
    --stage: #2b2d31;
    --blue-deep: #2f4f9a;
    --blue-mid: #4a6fc0;
    --blue-light: #7fa3dc;
    --ink-blue: #264a9c;
    --band-black: #141414;
    --band-rule: #9a9a9a;
    --paper: #ffffff;
    --text-light: #ffffff;
  }
  * { margin: 0; padding: 0; box-sizing: border-box; }
  html, body {
    width: 1200px; height: 901px; overflow: hidden;
    background: var(--stage);
    font-family: "Roboto", Arial, sans-serif;
  }
  .canvas {
    position: relative; width: 1200px; height: 901px;
    display: flex; flex-direction: column; align-items: center;
    justify-content: center; gap: 40px;
  }
  .card {
    position: relative; width: 700px; height: 400px; overflow: hidden;
    box-shadow: 0 10px 30px rgba(0,0,0,.45);
  }

  /* Back side */
  .card-back {
    background: radial-gradient(ellipse at 40% 35%, var(--blue-light) 0%, var(--blue-mid) 45%, var(--blue-deep) 100%);
    display: flex; flex-direction: column; align-items: center; justify-content: center;
    color: var(--text-light);
  }
  .brand { display: flex; align-items: center; gap: 16px; }
  .brand-dot { width: 34px; height: 34px; border-radius: 50%; background: currentColor; flex: none; }
  .brand-name { font-weight: 700; font-size: 58px; letter-spacing: -0.5px; line-height: 1; white-space: nowrap; }
  .brand-tagline {
    margin-top: 8px; font-weight: 500; font-size: 19px; letter-spacing: 2px;
    text-transform: uppercase; white-space: nowrap;
  }

  /* Front side */
  .card-front { background: var(--paper); }
  .front-head {
    height: 200px; display: flex; flex-direction: column; justify-content: center;
    padding-left: 130px; color: var(--ink-blue);
  }
  .front-head .brand-name { font-size: 52px; }
  .front-head .brand-dot { width: 30px; height: 30px; }
  .front-head .brand-tagline { font-size: 17px; margin-left: 46px; }
  .name-band {
    height: 42px; background: var(--band-black);
    border-top: 6px solid var(--band-rule);
    display: flex; align-items: center; justify-content: center;
    color: var(--text-light); font-weight: 700; font-size: 20px; letter-spacing: .5px;
  }
  .front-foot {
    height: 158px; font-style: normal;
    background: linear-gradient(180deg, var(--blue-light) 0%, var(--blue-mid) 55%, var(--blue-deep) 100%);
    color: var(--text-light); text-align: center; font-size: 15px; line-height: 1.45;
    padding-top: 18px;
  }
  .contact-gap { height: 10px; }
</style>
</head>
<body>
<main class="canvas">
  <section class="card card-back" aria-label="Business card back">
    <div class="brand">
      <span class="brand-dot"></span>
      <span class="brand-name">Forge Vexa</span>
    </div>
    <p class="brand-tagline">Shaping Steel Forward</p>
  </section>

  <section class="card card-front" aria-label="Business card front">
    <header class="front-head">
      <div class="brand">
        <span class="brand-dot"></span>
        <span class="brand-name">Forge Vexa</span>
      </div>
      <p class="brand-tagline">Shaping Steel Forward</p>
    </header>
    <div class="name-band">Gerald Pinwick</div>
    <address class="front-foot">
      <p>27615 Harlow Ave Unit C</p>
      <p>Alder Falls, WY 80519</p>
      <div class="contact-gap"></div>
      <p>P: 303-555-0182 &nbsp;|&nbsp; C: 303-555-0247</p>
      <p>E: gpinwick@forgevx.com &nbsp;|&nbsp; www.forgevx.com</p>
    </address>
  </section>
</main>
</body>
</html>
```